Business Card Design

A card that's appealing to realtors and home buyers..
Something that's memorable,attractive, yet simple.

Home Inspection business.
Name of co. Birchwell Home Inspections
Serving Kern, Los Angeles, Santa Barbara & Ventura counties
NRQB Certified Inspectors (Use NRQB certified logo)
http://nrqb-example.com/logos/newlogos/NRQB_Logo008.gif
Mark Ollivane
555 314-2760
Gavin Ollivane
555 492-1835
Email :birchwellinspections@mailbox-example.com
Also use slogan: Providing peace of mind

```html
<!DOCTYPE html>
<html lang="en">
<head>
<meta charset="utf-8">
<title>Birchwell Home Inspections – Business Card</title>
<link href="https://fonts.googleapis.com/css2?family=Montserrat:wght@500;700;800&family=Open+Sans:wght@400;600&display=swap" rel="stylesheet">
<style>
  :root{
    --page:#e9ebee;
    --card:#ffffff;
    --navy:#0f2f57;
    --blue-deep:#0a4f94;
    --blue:#1688d2;
    --blue-light:#3ab6ec;
    --charcoal:#2f3033;
    --ink:#3a3d42;
    --muted:#6b7078;
  }
  *{margin:0;padding:0;box-sizing:border-box}
  html,body{width:1200px;height:682px;overflow:hidden;background:var(--page)}
  .canvas{width:1200px;height:682px;display:flex;align-items:center;justify-content:center}
  .card{position:relative;width:840px;height:480px;background:var(--card);overflow:hidden;
        box-shadow:0 10px 30px rgba(0,0,0,.18)}
  .top-band{position:absolute;left:0;top:0;width:100%;height:18px;
        background:linear-gradient(90deg,var(--blue-deep),var(--blue) 55%,var(--blue-light))}
  .top-band-tab{position:absolute;right:0;top:18px;width:300px;height:8px;background:var(--navy)}
  .side-accent{position:absolute;left:0;top:18px;width:14px;height:382px;
        background:linear-gradient(180deg,var(--blue),var(--blue-light))}

  .role{position:absolute;right:44px;top:50px;font-family:"Montserrat",sans-serif;font-weight:500;
        font-size:16px;letter-spacing:3px;color:var(--blue);text-transform:uppercase}

  .brand{position:absolute;left:62px;top:70px;display:flex;align-items:center;gap:26px}
  .brand-dot{width:112px;height:112px;border-radius:50%;background:var(--blue);flex:none}
  .brand-name{font-family:"Montserrat",sans-serif;font-weight:800;color:var(--navy);
        font-size:30px;line-height:1.15;letter-spacing:4px;text-transform:uppercase}
  .slogan{margin-top:10px;font-family:"Open Sans",sans-serif;font-weight:400;font-size:16px;
        letter-spacing:1px;color:var(--muted)}

  .certification{position:absolute;right:44px;top:100px;width:130px;display:flex;flex-direction:column;
        align-items:center;gap:10px;text-align:center}
  .cert-badge{width:72px;height:72px;border-radius:50%;background:var(--navy)}
  .cert-caption{font-family:"Open Sans",sans-serif;font-weight:600;font-size:13px;line-height:1.3;
        color:var(--navy)}

  .person{position:absolute;left:62px;top:238px;display:flex;align-items:center;gap:8px}
  .person-icon{width:44px;height:44px;background:var(--charcoal);display:flex;align-items:center;justify-content:center}
  .person-name{height:44px;width:450px;display:flex;align-items:center;padding-left:22px;
        background:linear-gradient(90deg,var(--navy),var(--blue-deep) 60%,var(--blue));
        font-family:"Montserrat",sans-serif;font-weight:700;font-size:20px;letter-spacing:3px;
        color:#fff;text-transform:uppercase;white-space:nowrap}

  .contacts{position:absolute;left:62px;top:312px;display:grid;grid-template-columns:230px 1fr;
        row-gap:14px;column-gap:20px;list-style:none;
        font-family:"Open Sans",sans-serif;font-size:15px;color:var(--ink)}
  .contact{display:flex;align-items:center;gap:10px;white-space:nowrap}
  .contact svg{flex:none}
  .contact-label{font-weight:600;color:var(--navy)}

  .service-band{position:absolute;left:0;bottom:0;width:100%;height:80px;background:var(--charcoal);
        display:flex;align-items:center;gap:14px;padding-left:62px;
        font-family:"Open Sans",sans-serif;font-size:16px;color:#fff;letter-spacing:.5px}
  .service-band::before{content:"";position:absolute;left:0;top:0;width:100%;height:5px;
        background:linear-gradient(90deg,var(--blue-deep),var(--blue-light))}
</style>
</head>
<body>
<main class="canvas">
  <article class="card">
    <div class="top-band"></div>
    <div class="top-band-tab"></div>
    <div class="side-accent"></div>

    <p class="role">General Manager</p>

    <header class="brand">
      <div class="brand-dot"></div>
      <div>
        <h1 class="brand-name">Birchwell<br>Home Inspections</h1>
        <p class="slogan">Providing peace of mind</p>
      </div>
    </header>

    <aside class="certification">
      <div class="cert-badge" role="img" aria-label="Certification badge"></div>
      <p class="cert-caption">NRQB Certified Inspectors</p>
    </aside>

    <div class="person">
      <div class="person-icon">
        <svg width="24" height="24" viewBox="0 0 24 24" aria-hidden="true">
          <circle cx="12" cy="8" r="5" fill="#fff"/>
          <path d="M2 23c0-6 4.5-9 10-9s10 3 10 9z" fill="#fff"/>
        </svg>
      </div>
      <h2 class="person-name">Mark &amp; Gavin Ollivane</h2>
    </div>

    <ul class="contacts">
      <li class="contact">
        <svg width="18" height="18" viewBox="0 0 24 24" aria-hidden="true"><path fill="#1688d2" d="M6.6 10.8a15.1 15.1 0 006.6 6.6l2.2-2.2c.3-.3.7-.4 1-.2 1.1.4 2.3.6 3.6.6.6 0 1 .4 1 1V20c0 .6-.4 1-1 1A17 17 0 013 4c0-.6.4-1 1-1h3.5c.6 0 1 .4 1 1 0 1.3.2 2.5.6 3.6.1.3 0 .7-.2 1z"/></svg>
        <span class="contact-label">Mark</span> 555 314-2760
      </li>
      <li class="contact">
        <svg width="18" height="18" viewBox="0 0 24 24" aria-hidden="true"><rect x="2" y="5" width="20" height="14" rx="2" fill="#1688d2"/><path d="M3 6l9 7 9-7" stroke="#fff" stroke-width="2" fill="none"/></svg>
        birchwellinspections@mailbox-example.com
      </li>
      <li class="contact">
        <svg width="18" height="18" viewBox="0 0 24 24" aria-hidden="true"><path fill="#1688d2" d="M6.6 10.8a15.1 15.1 0 006.6 6.6l2.2-2.2c.3-.3.7-.4 1-.2 1.1.4 2.3.6 3.6.6.6 0 1 .4 1 1V20c0 .6-.4 1-1 1A17 17 0 013 4c0-.6.4-1 1-1h3.5c.6 0 1 .4 1 1 0 1.3.2 2.5.6 3.6.1.3 0 .7-.2 1z"/></svg>
        <span class="contact-label">Gavin</span> 555 492-1835
      </li>
      <li class="contact">
        <svg width="18" height="18" viewBox="0 0 24 24" aria-hidden="true"><circle cx="12" cy="12" r="10" fill="#1688d2"/><path d="M2 12h20M12 2c3 3 3 17 0 20M12 2c-3 3-3 17 0 20" stroke="#fff" stroke-width="1.5" fill="none"/></svg>
        www.birchwell-example.com
      </li>
    </ul>

    <footer class="service-band">
      <svg width="18" height="24" viewBox="0 0 18 24" aria-hidden="true"><path fill="#fff" d="M9 0a9 9 0 00-9 9c0 6.5 9 15 9 15s9-8.5 9-15a9 9 0 00-9-9zm0 12.5A3.5 3.5 0 1112.5 9 3.5 3.5 0 019 12.5z"/></svg>
      Serving Kern, Los Angeles, Santa Barbara &amp; Ventura counties
    </footer>
  </article>
</main>
</body>
</html>
```